Vorlen - Customer Experience Software Company Web Design

*****UPDATE*****
We've been getting a lot of corporate designs through. Unfortunately this is not what we are looking for. We would like our brand to be more approachable and for the look and feel to to be a bit more fun.
Also the best designs we have received so far have followed the "less is more" approach. Im hoping any news designs will take these aspects into account.
*****************

Background:

Vorlen is a Customer Experience Technology company. We equip business and technology teams with the frameworks, tools and services to help them create compelling experiences for their customers.

Our flagship product - Vorlen CX is an open-source customer experience application framework – it enables organisation to build highly differentiated business applications to deliver compelling experiences to your customers.

Vorlen CX is designed for innovators who understand that unlocking opportunity in today’s competitive marketplace is driven by delivering a better customer experience.

Task:

We are looking for a web design (we need PSD, no HTML/CSS) for our company site through which to launch our customer experience framework product. The site will be also used as a support site, so the functional aspect of the site is as important as the visual impact for sales.

In order to help us conceptualise ideas and content we have drafted a temporary website using a standard wordpress theme (please see details below). Now we have a general idea of our requirements we like we would like to take it to the next level and get some designs with that professional edge.

Our target market are Enterprise organisations - that is senior members of the business & technology teams (Business General Managers, CTO’s, CIO’s, and Senior Architects and Senior Developers). We want something clean & fresh which is DIFFERENT from the typical corporate technology websites out there. We would like to be seen as more approachable than most large technology companies.

Words we would like to use to describe the finished design:
• Clean (we’re thinking white background with one or two key colours)
• Fresh
• Light
• Modern
• Less is more
• Web 2.0
• Fun but professional (aimed at Enterprise/Large organisations)
• Bold, clear call to action – e.g. Live Demo & Download
• Readable (but Sans Serif)

As we’re a Customer Experience company, the usability of the site is critical. The site must be functional, intuitive & easy to navigate. We want to keep the number of user clicks to the bare minimum possible.

Other aspects, which we would like to incorporate into the site
• Home Page banner slider
• Client logon
• Newsletter sign up
• Social media links – Facebook, LinkedIn (for starters)
• Rich footer links

Some websites we like
• http://brightpanelworks.example - clean, light, modern & intuitive
• http://www.tamsoledrik.example - bold, clear messaging
• http://www.opengridhub.example/markup/emblem - punchy, colourful
• http://postwren.example/ - modern, clear messaging, colourful, rich footer area

Target Market(s)

Enterprise organisations - that is senior members of the business & technology teams (Business General Managers, CTO’s, CIO’s, Senior Devs)

Industry/Entity Type

Business

Requirements
Must have
• - Design Specs: Accepted file formats: During the design phase adobe PSD or JPEG are OK (if you need to upload files), but for the handover we'll need PSD only with all the original layers.
- The width needs to be a size that will work with every size computer screen
- Need to use cross-platform compatible font
- The graphic elements used for the design must be copyright free

Current test site
- URL http://vorlen.example/wp-admin
- username: artmarket
- password: artmarket

IMPORTANT NOTE REGARDING OUR CURRENT TEST SITE:

This is a very basic version of a site to help us generate requirements. This design is only a starting point/input and is not locked in stone i.e. we do not simply want this site simply tweaked around the edges.

We are looking for you to use all of your graphic design skills and experience to create a truly awesome site design!

```html
<!DOCTYPE html>
<html lang="en">
<head>
<meta charset="utf-8">
<title>Vorlen – The Customer Experience Framework</title>
<link rel="stylesheet" href="https://fonts.googleapis.com/css2?family=Source+Sans+3:wght@300;400;600&display=swap">
<style>
:root{
  --ink:#3a3a3a;
  --text:#555;
  --muted:#777;
  --brand-red:#e0302a;
  --heading-red:#cf3d1a;
  --orange:#f26b4c;
  --orange-dark:#d9522f;
  --page:#f7f7f7;
  --header:#efefef;
  --hero:#ececec;
  --dark:#1c1c1c;
  --line:#dedede;
  --box:#e8e8e8;
}
*{margin:0;padding:0;box-sizing:border-box}
html,body{width:1015px;height:1200px;overflow:hidden}
body{font-family:"Source Sans 3",Arial,sans-serif;background:var(--page);color:var(--text);position:relative}
.abs{position:absolute}
.topbar{left:0;top:0;width:1015px;height:12px;background:var(--dark)}
.header{left:0;top:12px;width:1015px;height:103px;background:var(--header);border-bottom:1px solid var(--line)}
.logo{left:73px;top:32px;font-size:38px;font-weight:300;color:var(--brand-red);line-height:1}
.tagline{left:73px;top:76px;font-size:11px;color:#444}
.nav a{position:absolute;top:18px;font-size:15px;color:#333;text-decoration:none}
.nav .active{left:403px;top:0;width:66px;height:49px;background:#222;color:#fff;border-radius:0 0 4px 4px;text-align:center;padding-top:18px}
.hero{left:0;top:116px;width:1015px;height:250px;background:var(--hero);border-bottom:3px solid #e2e2e2}
.arrow{width:50px;height:50px;border-radius:50%;background:#e0e0e0;border:4px solid #d2d2d2}
.hero-title{left:206px;top:144px;font-size:42px;font-weight:400;color:#444;line-height:1}
.hero-subtitle{left:202px;top:201px;font-size:18px;font-weight:400;color:#333;letter-spacing:.2px;line-height:22px}
.hero-text{left:203px;top:243px;width:300px;font-size:13px;line-height:19px;color:#444}
.btn{height:26px;background:var(--orange);border:1px solid var(--orange-dark);border-radius:4px;color:#3a1a10;font-size:13px;text-align:center;line-height:24px}
.chart{left:585px;top:150px;width:185px;height:175px;border-radius:6px;background:linear-gradient(160deg,#4fb4e6,#1d6fb8 60%,#2a3c96)}
.feature-icon{width:92px;height:104px;border-radius:8px}
.feature h3{position:absolute;font-size:16px;font-weight:400;color:var(--heading-red)}
.feature p{position:absolute;width:476px;font-size:11.3px;line-height:18.5px;text-align:justify;color:#444}
.login{left:686px;top:390px;width:259px;height:172px;background:var(--box);border-radius:8px;box-shadow:0 2px 3px rgba(0,0,0,.08)}
.login-tab{left:713px;top:384px;width:114px;height:38px;background:var(--orange);border-radius:0 0 4px 4px;color:#2a120a;font-size:13px;line-height:44px;padding-left:37px}
.field{background:#f6f6f6;border:1px solid #ddd;border-radius:14px;font-size:12px;color:#777;padding-left:15px}
.newsletter{left:686px;top:586px;width:259px;height:76px;background:var(--orange);border-radius:7px}
.like-title{left:696px;top:688px;width:250px;font-size:14px;line-height:17px;color:#555}
.avatar{width:40px;height:40px;border:2px solid #fff;box-shadow:0 0 1px #aaa}
.avatar-name{width:50px;text-align:center;font-size:7px;color:#666}
.platform{top:950px;font-size:26px;color:#888;font-weight:400;line-height:34px}
.footer-band{left:0;top:1020px;width:1015px;height:180px;background:#efefef;border-top:4px solid #e4e4e4}
.footer-col{position:absolute;top:1043px;list-style:none}
.footer-col li{font-size:12px;color:#555;height:22px;padding-left:11px;position:relative}
.footer-col li::before{content:"";position:absolute;left:0;top:6px;width:4px;height:4px;border-radius:50%;background:#777}
.social{top:1043px;width:20px;height:20px;border-radius:2px}
</style>
</head>
<body>
<div class="abs topbar"></div>
<header class="abs header"></header>
<div class="abs logo">Vorlen</div>
<div class="abs tagline">The Customer Experience Framework</div>
<nav class="nav abs" style="left:0;top:12px;width:1015px;height:50px">
  <a class="active">Home</a>
  <a style="left:500px">Products</a>
  <a style="left:601px">Support</a>
  <a style="left:697px">Blog</a>
  <a style="left:769px">About Us</a>
  <a style="left:873px">Contact Us</a>
</nav>

<section class="abs hero"></section>
<div class="abs arrow" style="left:75px;top:215px"><svg width="42" height="42"><path d="M24 13 L16 21 L24 29" stroke="#888" stroke-width="3" fill="none"/></svg></div>
<div class="abs arrow" style="left:875px;top:215px"><svg width="42" height="42"><path d="M18 13 L26 21 L18 29" stroke="#888" stroke-width="3" fill="none"/></svg></div>
<h1 class="abs hero-title">Standard chunk</h1>
<h2 class="abs hero-subtitle">LOREM IPSUM USED SINCE THE 1500S</h2>
<p class="abs hero-text">Cicero are also reproduced in their exact original form, accompanied by English</p>
<div class="abs btn" style="left:239px;top:307px;width:86px">VIEW DEMO</div>
<div class="abs btn" style="left:360px;top:307px;width:86px">VIEW MORE</div>
<div class="abs chart" role="img" aria-label="Illustration of a rising 3D bar chart with a pie chart and arrow"></div>

<div class="feature">
  <div class="abs feature-icon" style="left:77px;top:413px;background:#e4542a" role="img" aria-label="Markup standard emblem"></div>
  <h3 style="left:187px;top:408px">Cross platform - Web, Tablet and Mobile</h3>
  <p style="left:187px;top:439px">It is a long established fact that a reader will be distracted by the readable content of a page when looking at its layout. The point of using Lorem Ipsum is that it has a more-or-less normal distribution of letters, as opposed to using 'Content here, content here', making it look like readable English. Many desktop publishing packages and web page editors now use Lorem Ipsum as their default model text, and a search for 'lorem ipsum' will uncover many web sites still in their infancy. Various versions have evolved over the years, sometimes by accident, sometimes on purpose (injected humour and the like).</p>
</div>
<div class="feature">
  <div class="abs feature-icon" style="left:82px;top:606px;width:86px;height:114px;background:#3c9a46" role="img" aria-label="Open source approved licence badge"></div>
  <h3 style="left:187px;top:603px">Open Source</h3>
  <p style="left:187px;top:633px">It is a long established fact that a reader will be distracted by the readable content of a page when looking at its layout. The point of using Lorem Ipsum is that it has a more-or-less normal distribution of letters, as opposed to using 'Content here, content here', making it look like readable English. Many desktop publishing packages and web page editors now use Lorem Ipsum as their default model text, and a search for 'lorem ipsum' will uncover many web sites.</p>
</div>
<div class="feature">
  <div class="abs feature-icon" style="left:82px;top:773px;width:86px;height:82px;background:linear-gradient(#e23a2a,#b8211a)" role="img" aria-label="Red toolbox illustration"></div>
  <h3 style="left:187px;top:766px">Webforge Toolkit</h3>
  <p style="left:187px;top:796px">It is a long established fact that a reader will be distracted by the readable content of a page when looking at its layout. The point of using Lorem Ipsum is that it has a more-or-less normal distribution of letters, as opposed to using 'Content here, content here', making it look like readable English. Many desktop publishing packages and web page editors now use Lorem Ipsum as their default model text, and a search for 'lorem ipsum' will uncover many web sites still in their infancy. Various versions have evolved over the years.</p>
</div>

<aside>
  <div class="abs login"></div>
  <div class="abs login-tab"><svg class="abs" style="left:12px;top:10px" width="16" height="20"><rect x="1" y="8" width="14" height="11" fill="#1a1a1a"/><path d="M4 8 V5 a4 4 0 0 1 8 0 V8" stroke="#1a1a1a" stroke-width="2" fill="none"/></svg>Client Log in</div>
  <div class="abs field" style="left:715px;top:444px;width:208px;height:30px;line-height:28px">Username</div>
  <div class="abs field" style="left:715px;top:483px;width:208px;height:31px;line-height:29px">*********</div>
  <div class="abs" style="left:744px;top:532px;width:9px;height:9px;border:1px solid #aaa;background:#fff"></div>
  <div class="abs" style="left:760px;top:529px;font-size:11.5px;color:#444">Remember Me</div>
  <div class="abs btn" style="left:847px;top:523px;width:64px;height:25px;border-radius:13px;line-height:23px;font-size:12px">Log in</div>

  <div class="abs newsletter"></div>
  <div class="abs" style="left:699px;top:595px;font-size:13px;color:#2a120a">News Letter Log In</div>
  <div class="abs field" style="left:698px;top:622px;width:237px;height:28px;line-height:26px;background:#fafafa;font-size:11px;padding-left:13px">Enter your mail ID</div>
  <div class="abs" style="left:882px;top:629px;width:47px;height:16px;border-radius:8px;background:#444;color:#fff;font-size:9px;text-align:center;line-height:16px">Submit</div>

  <div class="abs like-title">Like our page and win a bundle of <b style="font-weight:600;color:#333">150 files</b> collection of our best graphics <span style="color:#e08a2a">?</span></div>
  <svg class="abs" style="left:905px;top:712px" width="16" height="14"><path d="M2 2 H10 V11 M7 8 L10 11 L13 8" stroke="#444" stroke-width="1.4" fill="none"/></svg>
  <div class="abs" style="left:696px;top:737px;font-size:8px;color:#555">347 people like <b style="font-weight:600;color:#333">Pixel Grove</b>.</div>
  <div class="abs" style="left:869px;top:732px;width:68px;height:16px;background:#e6ebf4;border:1px solid #bfc9dc;font-size:8px;color:#3b5a98;padding-left:16px;line-height:14px">Like</div>

  <div class="abs avatar" style="left:696px;top:761px;background:#6fb4c8" role="img" aria-label="Member photo"></div>
  <div class="abs avatar" style="left:746px;top:761px;background:#8a5a44" role="img" aria-label="Member photo"></div>
  <div class="abs avatar" style="left:796px;top:761px;background:#7ea26a" role="img" aria-label="Member photo"></div>
  <div class="abs avatar" style="left:846px;top:761px;background:#e8e0e4" role="img" aria-label="Member avatar artwork"></div>
  <div class="abs avatar" style="left:896px;top:761px;background:#d6e8a0" role="img" aria-label="Member avatar artwork"></div>
  <div class="abs avatar-name" style="left:691px;top:806px">Nadia</div>
  <div class="abs avatar-name" style="left:741px;top:806px">Stavro</div>
  <div class="abs avatar-name" style="left:791px;top:806px">Orin</div>
  <div class="abs avatar-name" style="left:841px;top:806px">Marlow</div>
  <div class="abs avatar-name" style="left:891px;top:806px">Melisa</div>
  <div class="abs avatar" style="left:696px;top:821px;background:#2a2a2a" role="img" aria-label="Member photo"></div>
  <div class="abs avatar" style="left:746px;top:821px;background:#9a9a8a" role="img" aria-label="Member photo"></div>
  <div class="abs avatar" style="left:796px;top:821px;background:#f0f0f0" role="img" aria-label="Member avatar artwork"></div>
  <div class="abs avatar" style="left:846px;top:821px;background:#8a8a8a" role="img" aria-label="Member photo"></div>
  <div class="abs avatar" style="left:896px;top:821px;background:#a8a0c8" role="img" aria-label="Member avatar artwork"></div>
  <div class="abs avatar-name" style="left:691px;top:866px">Kovalin</div>
  <div class="abs avatar-name" style="left:741px;top:866px">Kasim</div>
  <div class="abs avatar-name" style="left:791px;top:866px">Manoret</div>
  <div class="abs avatar-name" style="left:841px;top:866px">Sandrel</div>
  <div class="abs avatar-name" style="left:891px;top:866px">Mirolan</div>
  <div class="abs" style="left:696px;top:886px;width:244px;height:5px;background:repeating-linear-gradient(135deg,#ddd 0 2px,transparent 2px 4px)"></div>
</aside>

<div class="abs platform" style="left:93px">Pocketa</div>
<div class="abs platform" style="left:206px;font-size:17px">Robotin</div>
<div class="abs platform" style="left:280px;font-size:23px">Duskberry</div>
<div class="abs platform" style="left:443px">tileOS</div>
<div class="abs platform" style="left:566px">kora</div>

<footer class="abs footer-band"></footer>
<ul class="footer-col" style="left:83px"><li>Home</li><li>About Us</li><li>View Demo</li><li>Download</li></ul>
<ul class="footer-col" style="left:194px"><li>Partners</li><li>Our Products</li><li>Our Services</li><li>Testimonials</li></ul>
<ul class="footer-col" style="left:315px"><li>Customer Support</li><li>Blog Archieves</li><li>Contact Us</li></ul>
<ul class="footer-col" style="left:463px"><li>Terms of use</li><li>Privacy Policy</li><li>Copyright Policy</li></ul>
<div class="abs" style="left:665px;top:1046px;font-size:12px;color:#444">Connect with us :</div>
<div class="abs social" style="left:772px;background:#3b5998"></div>
<div class="abs social" style="left:809px;background:#5bc0eb"></div>
<div class="abs social" style="left:846px;background:#f57d00"></div>
<div class="abs social" style="left:882px;background:#0e76a8"></div>
<div class="abs social" style="left:919px;background:#4a9d3a"></div>
<div class="abs" style="left:672px;top:1088px;font-size:31px;font-weight:300;color:#888;line-height:1">Vorlen</div>
<div class="abs" style="left:768px;top:1107px;font-size:11px;color:#555">The Customer Experience Framework</div>
<div class="abs" style="left:0;top:1152px;width:1015px;text-align:center;font-size:12px;color:#222">Copyright © 2011 www.vorlen.example &nbsp; All rights reserved</div>
</body>
</html>
```